Global Aviation Services website

we are a start up airline/aviation services company that will operate in Australia, USA and New Zealand initially. Fundamentally the service is to airlines who fly into and out of a market yet do not wish to have their own admin, sales and marketing infrastructures. They would use us.
The company name is Tovelle.
It needs to look sophisticated, sharp and professional. We would like it designed and built in the CMS - wordpress so we can update after the project is finished when necessary. An example of who we are and a good website we like can be found at: http://brenmorcrest.com/. There is no ecommerce or interactivity other than a contact us. We do like animation for promotion. There will be links to our airline clients and sub sites or pages will exist for the various offices we have globally. Currently 6. Each of these offices will have a dedicated local URL. Please submit your suggestion of a home page and 2 internal pages. Thank you and kind regards Ingrid
Target Market(s)
airlines, airline technology companies,
Industry/Entity Type
Aviation
Coding
Coded - Design and coding required
Number of Pages Required
5+ page
Font styles to use
Look and feel

```html
<!DOCTYPE html>
<html lang="en">
<head>
<meta charset="utf-8">
<title>Tovelle — About Us</title>
<link href="https://fonts.googleapis.com/css2?family=Raleway:wght@400;500;700&family=Open+Sans:wght@400;600;700&display=swap" rel="stylesheet">
<style>
  :root{
    --brand-blue:#0a55a7;
    --brand-blue-deep:#0b4f9c;
    --ink:#1b1b1b;
    --body-text:#6a6a6a;
    --white:#ffffff;
    --sky-light:#c9d4de;
    --sky-mid:#8ea3b6;
    --accent-red:#e3222a;
  }
  *{box-sizing:border-box;margin:0;padding:0}
  html,body{width:1200px;height:1117px;overflow:hidden;background:var(--white)}
  body{position:relative;font-family:"Open Sans",Arial,sans-serif;color:var(--ink)}

  .site-header{position:absolute;left:0;top:0;width:1200px;height:66px;background:var(--white)}
  .brand{position:absolute;left:89px;top:18px;display:flex;align-items:center;gap:8px;
    font-family:"Raleway",Arial,sans-serif;font-weight:700;font-size:27px;color:var(--brand-blue-deep);letter-spacing:.5px}
  .brand-dot{width:14px;height:14px;border-radius:50%;background:var(--brand-blue-deep)}
  .main-nav{position:absolute;top:0;left:0;height:66px}
  .main-nav a{position:absolute;top:0;height:66px;line-height:68px;font-size:12px;color:var(--ink);text-decoration:none}
  .nav-home{left:801px}
  .nav-about{left:852px;width:75px;text-align:center;background:var(--brand-blue);color:var(--white)!important;font-weight:700}
  .nav-new{left:946px}
  .nav-contact{left:1011px}
  .nav-search{position:absolute;left:1096px;top:26px}

  .page-banner{position:absolute;left:0;top:66px;width:1200px;height:117px;
    background:linear-gradient(180deg,#aab8c6 0%,var(--sky-light) 35%,var(--sky-mid) 75%,#7d91a3 100%)}
  .page-banner svg{position:absolute;left:0;top:0}
  .page-title{position:absolute;left:89px;top:46px;font-family:"Raleway",Arial,sans-serif;font-weight:700;font-size:32px;color:var(--white)}

  .photo{position:absolute}
  .photo-tower{left:91px;top:276px;width:281px;height:372px;background:linear-gradient(160deg,#3b4f6b,#6f8cb0 50%,#1f2d44)}
  .photo-aircraft{left:240px;top:214px;width:205px;height:269px;background:linear-gradient(180deg,#b9c9d6 0%,#dfe3e6 45%,#8f948e 100%)}

  .section-title{position:absolute;font-family:"Raleway",Arial,sans-serif;font-weight:400;font-size:23px;color:var(--ink);line-height:1}
  .section-title strong{font-weight:700;color:var(--brand-blue)}
  .company-title{left:517px;top:239px}
  .team-title{left:88px;top:697px}

  .company-copy{position:absolute;left:516px;width:598px;font-size:11.6px;line-height:22.2px;color:var(--body-text)}
  .copy-one{top:274px}
  .copy-two{top:450px}

  .slider-arrow{position:absolute;top:695px;width:26px;height:26px;border-radius:50%}
  .arrow-prev{left:1054px;border:1px solid var(--ink)}
  .arrow-next{left:1085px;border:1px solid var(--brand-blue)}
  .slider-arrow svg{position:absolute;left:8px;top:7px}

  .team-card{position:absolute;top:744px;width:256px}
  .team-photo{width:256px;height:256px}
  .team-name{margin-top:12px;font-family:"Raleway",Arial,sans-serif;font-size:13.5px;color:var(--ink)}
  .card-1{left:90px}.card-1 .team-photo{background:linear-gradient(135deg,#c99b2c,#6d6b67 45%,#cfcac2)}
  .card-2{left:346px}.card-2 .team-photo{background:linear-gradient(160deg,#2f6fc4,#8fb5dc 50%,#3a3f4a)}
  .card-3{left:602px}.card-3 .team-photo{position:relative;background:linear-gradient(160deg,#1a5cab,#0b4f9e)}
  .card-4{left:858px}.card-4 .team-photo{background:linear-gradient(160deg,#7c8590,#b8ad98 50%,#6b7178)}
  .social-links{position:absolute;left:57px;top:109px;display:flex;gap:8px}
  .social-links span{width:42px;height:42px;border-radius:50%;background:var(--white)}
  .social-links span.is-active{background:var(--accent-red)}

  .site-footer{position:absolute;left:0;top:1064px;width:1200px;height:53px;background:var(--brand-blue);color:var(--white);font-size:12px}
  .copyright{position:absolute;left:89px;top:19px}
  .footer-links{position:absolute;left:903px;top:19px;display:flex;gap:14px}
  .footer-links a{color:var(--white);text-decoration:none}
</style>
</head>
<body>
  <header class="site-header">
    <div class="brand"><span class="brand-dot"></span>Tovelle</div>
    <nav class="main-nav">
      <a class="nav-home" href="#">HOME</a>
      <a class="nav-about" href="#">ABOUT</a>
      <a class="nav-new" href="#">NEW</a>
      <a class="nav-contact" href="#">CONTACT</a>
    </nav>
    <svg class="nav-search" width="16" height="16" viewBox="0 0 16 16" aria-label="Search">
      <circle cx="6" cy="6" r="4.5" fill="none" stroke="#1b1b1b" stroke-width="1.8"/>
      <line x1="9.3" y1="9.3" x2="14.5" y2="14.5" stroke="#1b1b1b" stroke-width="2.4" stroke-linecap="round"/>
    </svg>
  </header>

  <section class="page-banner" role="img" aria-label="Aerial view of clouds above land">
    <svg width="1200" height="117" viewBox="0 0 1200 117"><polygon points="0,0 402,0 466,117 0,117" fill="#0a55a7"/></svg>
    <h1 class="page-title">ABOUT US</h1>
  </section>

  <div class="photo photo-tower" role="img" aria-label="Glass skyscrapers seen from below"></div>
  <div class="photo photo-aircraft" role="img" aria-label="Passenger jet parked at an airport gate with a tug"></div>

  <h2 class="section-title company-title">ABOUT THE <strong>COMPANY</strong></h2>
  <p class="company-copy copy-one">Lorem ipsum dolor sit amet, consectetuer adipiscing elit. Aenean commodo ligula eget dolor. Aenean massa. Cum sociis natoque penatibus et magnis dis parturient montes, nascetur ridiculus mus. Donec quam felis, ultricies nec, pellentesque eu, pretium quis, sem. Nulla consequat massa quis enim. Donec pede justo, fringilla vel, aliquet nec, vulputate eget, arcu. In enim justo, rhoncus ut, imperdiet a, venenatis vitae, justo. Nullam dictum felis eu pede mollis pretium. Integer tincidunt. Cras dapibus. Vivamus elementum semper nisi. Aenean vulputate eleifend tellus. Aenean leo ligula, porttitor eu, consequat vitae, eleifend ac, enim. Aliquam lorem ante, dapibus in, viverra quis, feugiat a, tellus.</p>
  <p class="company-copy copy-two">Aenean vulputate eleifend tellus. Aenean leo ligula, porttitor eu, consequat vitae, eleifend ac, enim. Aliquam Nam quam nunc, blandit vel, luctus pulvinar, hendrerit id, lorem. Maecenas nec odio et ante tincidunt tempus. Donec vitae sapien ut libero venenatis faucibus. Nullam quis ante. Etiam sit amet orci eget eros faucibus tincidunt. Duis leo. Sed fringilla mauris sit amet nibh. Donec sodales sagittis magna. Sed consequat, leo eget bibendum sodales, augue velit cursus nunc nam quam nunc, blandit vel, luctus pulvinar, hendrerit id, lorem. Maecenas nec odio et ante tincidunt tempus. Donec vitae sapien ut libero venenatis faucibus. Nullam quis ante. Etiam sit amet orci eget eros faucibus tincidunt. Duis leo. Sed fringilla mauris sit amet nibh. Donec sodales sagittis magna. Sed consequat, leo eget bibendum sodales, augue velit cursus nunc.</p>

  <h2 class="section-title team-title">MEET THE <strong>TEAM</strong></h2>
  <span class="slider-arrow arrow-prev"><svg width="10" height="12" viewBox="0 0 10 12"><polyline points="7,1 2,6 7,11" fill="none" stroke="#1b1b1b" stroke-width="1.3"/></svg></span>
  <span class="slider-arrow arrow-next"><svg width="10" height="12" viewBox="0 0 10 12"><polyline points="3,1 8,6 3,11" fill="none" stroke="#0a55a7" stroke-width="1.3"/></svg></span>

  <article class="team-card card-1">
    <div class="team-photo" role="img" aria-label="Team member seated in a helicopter cockpit"></div>
    <h3 class="team-name">JOHN DOE</h3>
  </article>
  <article class="team-card card-2">
    <div class="team-photo" role="img" aria-label="Team member flying a glider above the clouds"></div>
    <h3 class="team-name">MARK DOE</h3>
  </article>
  <article class="team-card card-3">
    <div class="team-photo" role="img" aria-label="Team member portrait under a blue overlay">
      <div class="social-links"><span></span><span class="is-active"></span><span></span></div>
    </div>
    <h3 class="team-name">GEORGE DOE</h3>
  </article>
  <article class="team-card card-4">
    <div class="team-photo" role="img" aria-label="Team member in vintage flight gear beside an aircraft"></div>
    <h3 class="team-name">ELIOT DOE</h3>
  </article>

  <footer class="site-footer">
    <p class="copyright">©2016 Tovelle, All Rights Reserved</p>
    <nav class="footer-links"><a href="#">Privacy Policy</a><span>|</span><a href="#">Terms &amp; Conditions</a></nav>
  </footer>
</body>
</html>
```